Creative, fresh business card design for Brindlecrest Linings

We need a fresh, creative business card design for Brindlecrest Linings. We are the manufacturer of Brindlecrest Linings in Australia. Wall panels are 2400 x 1200mm panels made from MDF and feature 3D patterns on the face of the panel. The colours to be used are green, silver/grey and white RGB
Red 187
Green 207
Blue 65.

An idea is to possibly use a watermark of one of our designs as a background (like on the "Lattice" design on the left hand side of page 2 of our brochure).

Target Market(s)

Interior designers, architects, builders and home renovators

Industry/Entity Type

Business

Contact Information for Business Card

Details to go on the card are:
Our logo (attached),
Slogan: "Decorative panels for interiors and exteriors",
Contact name,
Position,
Mobile phone number,
Business address,
Business phone,
Business fax,
Website and
Email address.

I have attached a few images of our panels and our brochure for reference.

The colours of the business card should feature our logo colours which are: RGB
Red 187
Green 207
Blue 65

Requirements
Must have
• Very modern fonts and design. Some of the designs shown especially the "Weave" design which is a popular design.
Nice to have
• Creative but simple design. Very contemporary.
Should not have
• Anything ornate or old fashioned.

```html
<!DOCTYPE html>
<html lang="en">
<head>
<meta charset="utf-8">
<title>Brindlecrest Linings – Business Cards</title>
<link href="https://fonts.googleapis.com/css2?family=Roboto+Condensed:wght@400;700&family=Roboto:wght@300;400&display=swap" rel="stylesheet">
<style>
  :root{
    --green:#bbcf41;
    --grey:#8f9091;
    --white:#ffffff;
    --tag:#6b6c6d;
    --page:#eceeed;
  }
  *{box-sizing:border-box;margin:0;padding:0}
  html,body{width:1200px;height:1200px;overflow:hidden;background:var(--page)}
  .sheet{
    position:absolute;left:72px;top:100px;
    display:grid;grid-template-columns:515px 515px;grid-template-rows:315px 315px 315px;
    column-gap:28px;row-gap:27px;
  }
  .card{position:relative;width:515px;height:315px;background:var(--white);font-family:"Roboto Condensed",sans-serif}
  .card__person{
    position:absolute;left:0;top:0;width:194px;height:153px;background:var(--green);color:var(--white);
    padding:40px 0 0 20px;font-size:16px;line-height:21px;
  }
  .card__name{font-weight:700}
  .card__mobile{font-weight:700;margin-top:22px}
  .card__photo{
    position:absolute;left:198px;top:0;width:317px;height:153px;
    background:linear-gradient(100deg,#3a3a3a 0%,#8a8a8a 20%,#4a4a4a 40%,#9a9a9a 60%,#5c5c5c 78%,#c9c2b4 88%,#dcd6cc 100%);
  }
  .card__tagline{
    position:absolute;left:0;top:153px;width:515px;height:39px;
    font-family:"Roboto",sans-serif;font-weight:300;font-size:16px;letter-spacing:3.4px;
    color:var(--tag);text-align:center;line-height:39px;
  }
  .card__brandmark{position:absolute;left:0;top:192px;width:194px;height:77px;background:var(--green)}
  .card__brandmark-square{position:absolute;left:20px;top:20px;width:38px;height:38px;background:var(--white)}
  .card__brand{
    position:absolute;left:0;top:272px;width:194px;height:43px;background:var(--grey);
    color:var(--white);font-size:18px;font-weight:400;line-height:43px;text-align:center;
  }
  .card__contact{
    position:absolute;left:198px;top:192px;width:317px;height:123px;background:var(--grey);
    color:var(--white);padding:12px 0 0 14px;font-size:16px;line-height:25px;
  }
  .card__contact .strong{font-weight:700}
</style>
</head>
<body>
<main class="sheet">

  <article class="card">
    <div class="card__person"><div class="card__name">Carina Westhaven</div><div>Director</div><div class="card__mobile">M 0400 118 203</div></div>
    <div class="card__photo" role="img" aria-label="Photo of a grey wave-patterned wall panel in a dining interior"></div>
    <div class="card__tagline">decorative panels for interiors &amp; exteriors</div>
    <div class="card__brandmark"><span class="card__brandmark-square"></span></div>
    <div class="card__brand">Brindlecrest Linings</div>
    <div class="card__contact"><div class="strong">P 02 9000 1100&nbsp; F 02 9000 1177</div><div>14 Harlow Street, Kelmscott Park 2170</div><div>carina@brindlecrest.com.au</div><div class="strong">www.brindlecrest.com.au</div></div>
  </article>

  <article class="card">
    <div class="card__person"><div class="card__name">Tomas Westhaven</div><div>Director</div><div class="card__mobile">M 0400 118 204</div></div>
    <div class="card__photo" role="img" aria-label="Photo of a grey wave-patterned wall panel in a dining interior"></div>
    <div class="card__tagline">decorative panels for interiors &amp; exteriors</div>
    <div class="card__brandmark"><span class="card__brandmark-square"></span></div>
    <div class="card__brand">Brindlecrest Linings</div>
    <div class="card__contact"><div class="strong">P 02 9000 1100&nbsp; F 02 9000 1177</div><div>14 Harlow Street, Kelmscott Park 2170</div><div>tomas@brindlecrest.com.au</div><div class="strong">www.brindlecrest.com.au</div></div>
  </article>

  <article class="card">
    <div class="card__person"><div class="card__name">Julian Westhaven</div><div>General Manager</div><div class="card__mobile">M 0400 326 415</div></div>
    <div class="card__photo" role="img" aria-label="Photo of a grey wave-patterned wall panel in a dining interior"></div>
    <div class="card__tagline">decorative panels for interiors &amp; exteriors</div>
    <div class="card__brandmark"><span class="card__brandmark-square"></span></div>
    <div class="card__brand">Brindlecrest Linings</div>
    <div class="card__contact"><div class="strong">P 02 9000 1100&nbsp; F 02 9000 1177</div><div>14 Harlow Street, Kelmscott Park 2170</div><div>julian@brindlecrest.com.au</div><div class="strong">www.brindlecrest.com.au</div></div>
  </article>

  <article class="card">
    <div class="card__person"><div class="card__name">Owen Marsh</div><div>Production Manager</div><div class="card__mobile">M 0400 327 580</div></div>
    <div class="card__photo" role="img" aria-label="Photo of a grey wave-patterned wall panel in a dining interior"></div>
    <div class="card__tagline">decorative panels for interiors &amp; exteriors</div>
    <div class="card__brandmark"><span class="card__brandmark-square"></span></div>
    <div class="card__brand">Brindlecrest Linings</div>
    <div class="card__contact"><div class="strong">P 02 9000 1100&nbsp; F 02 9000 1177</div><div>14 Harlow Street, Kelmscott Park 2170</div><div>sales@brindlecrest.com.au</div><div class="strong">www.brindlecrest.com.au</div></div>
  </article>

  <article class="card">
    <div class="card__person"><div class="card__name">Nadia Marsh</div><div>Sales/Admin</div><div class="card__mobile">M 0400 329 612</div></div>
    <div class="card__photo" role="img" aria-label="Photo of a grey wave-patterned wall panel in a dining interior"></div>
    <div class="card__tagline">decorative panels for interiors &amp; exteriors</div>
    <div class="card__brandmark"><span class="card__brandmark-square"></span></div>
    <div class="card__brand">Brindlecrest Linings</div>
    <div class="card__contact"><div class="strong">P 02 9000 1100&nbsp; F 02 9000 1177</div><div>14 Harlow Street, Kelmscott Park 2170</div><div>sales@brindlecrest.com.au</div><div class="strong">www.brindlecrest.com.au</div></div>
  </article>

  <article class="card">
    <div class="card__person"><div class="card__name">Elena Pavlides</div><div>Sales/Admin</div><div class="card__mobile">M 0400 441 739</div></div>
    <div class="card__photo" role="img" aria-label="Photo of a grey wave-patterned wall panel in a dining interior"></div>
    <div class="card__tagline">decorative panels for interiors &amp; exteriors</div>
    <div class="card__brandmark"><span class="card__brandmark-square"></span></div>
    <div class="card__brand">Brindlecrest Linings</div>
    <div class="card__contact"><div class="strong">P 02 9000 1100&nbsp; F 02 9000 1177</div><div>14 Harlow Street, Kelmscott Park 2170</div><div>sales@brindlecrest.com.au</div><div class="strong">www.brindlecrest.com.au</div></div>
  </article>

</main>
</body>
</html>
```